Chocolate company needing sticker for products

I have a small chocolate company Willow Bend Sweets in Austin Texas. I make all vegan, gluten free, organic, faire trade chocolate that tastes amazing! It is allergy friendly approvable by all ages. I want to have a great sticker that i can put on our boxes and bags. I am using a lot of natural craft color and brown. I am open to color options possibly for different flavors. I want the packaging to reflect the basis of my company. It is all handmade by me but i don't want it to have to much of a crafty look to it. I have attached the logo designs I have. it the sticker can have som of the bullet points about the company that would be great. But it needs to say Locally Made in Austin Texas. it also has to have the company address.
418 West Cobbler Ridge Rd #207 Austin Tx 78745. These things are required by the state for food regulations. I want something that looks great and I can be really proud to put on my product! Thanks so much for all of your help in advance. Dot

I also need some other information added to the sticker. Website which is willowbendsweetsatx.com 

Phone number 512.368.4175. Instagram willowbendsweets. Thanks for your hard work! 

Industry/Entity Type

Chocolate Company

Requirements
Must have
• The logo is added at the bottom as well as designs I like I want to have a professional look but it to be approvable by all consumers. I will gig feed back as i see what designs come through. This will probably fold out into a multi design project so i will be looking for assistance on other areas of this as well. Thanks

```html
<!DOCTYPE html>
<html lang="en">
<head>
<meta charset="utf-8">
<title>Willow Bend Sweets – Product Stickers</title>
<link rel="stylesheet" href="https://fonts.googleapis.com/css2?family=Oswald:wght@400;500;600&display=swap">
<style>
  :root{
    --backdrop:#2a2a2a;
    --ink-dark:#231510;
    --purple:#6e3b86;
    --teal:#1f6b78;
    --olive:#7c8c3a;
    --yellow:#d9c02a;
    --orange:#d58a2e;
    --wine:#8a2a3a;
    --kraft:#c8a57a;
    --kraft-ink:#3a2214;
  }
  *{box-sizing:border-box;margin:0;padding:0}
  html,body{width:1200px;height:1000px;overflow:hidden;background:var(--backdrop)}
  body{font-family:"Oswald",sans-serif}
  .sheet{position:relative;width:1200px;height:1000px;display:flex;justify-content:center;align-items:center;gap:36px}

  .sticker{
    position:relative;width:252px;height:600px;border-radius:26px;
    background:var(--bg);color:var(--ink);overflow:hidden;
    display:flex;flex-direction:column;align-items:center;
    padding:14px 14px 20px;
  }
  .sticker::after{
    content:"";position:absolute;inset:8px;border:2px solid var(--ink);
    border-radius:20px;pointer-events:none;opacity:.85;
  }
  .sticker--purple{--bg:var(--purple);--ink:var(--ink-dark)}
  .sticker--teal{--bg:var(--teal);--ink:var(--ink-dark)}
  .sticker--yellow{--bg:var(--yellow);--ink:var(--ink-dark)}
  .sticker--kraft{--bg:var(--kraft);--ink:var(--kraft-ink)}

  .flavour{
    width:100%;font-weight:500;font-size:19px;letter-spacing:.5px;
    text-transform:uppercase;line-height:1;text-align:left;
    padding:6px 8px 6px;transform:rotate(-5deg);transform-origin:left bottom;
  }
  .flavour-bar{width:112%;height:12px;background:var(--ink);transform:rotate(-5deg);margin:0 0 4px -6%}
  .flavour-rule{width:100%;height:3px;background:var(--ink);margin-bottom:14px}

  .brand-row{display:flex;align-items:center;gap:8px;width:100%;justify-content:space-between}
  .ornament-side{width:20px;height:64px;background:var(--ink);opacity:.55;border-radius:3px}
  .brand{
    font-weight:600;font-size:34px;line-height:1.02;text-transform:uppercase;
    text-align:center;letter-spacing:.5px;
  }

  .claims{
    width:calc(100% + 4px);background:var(--ink);color:var(--bg);
    margin:16px 0 12px;padding:5px 4px;text-align:center;
    font-size:13.5px;line-height:1.5;letter-spacing:.4px;text-transform:uppercase;
  }
  .ornament-row{width:120px;height:12px;background:var(--ink);opacity:.55;border-radius:3px;margin:8px 0}

  .origin-lead{font-weight:500;font-size:15px;text-transform:uppercase;line-height:1.1;margin-top:4px}
  .origin{font-weight:600;font-size:27px;text-transform:uppercase;line-height:1.1}

  .address{font-weight:500;font-size:14.5px;text-transform:uppercase;text-align:center;line-height:1.35;margin-top:2px}
  .contact{font-size:14.5px;text-align:center;line-height:1.3;margin-top:2px}
</style>
</head>
<body>
<main class="sheet">

  <article class="sticker sticker--purple">
    <div class="flavour">Pecan Praline Bites</div>
    <div class="flavour-bar"></div>
    <div class="flavour-rule"></div>
    <div class="brand-row">
      <div class="ornament-side" role="img" aria-label="Tribal spiral ornament"></div>
      <h2 class="brand">Willow<br>Bend<br>Sweets</h2>
      <div class="ornament-side" role="img" aria-label="Tribal spiral ornament"></div>
    </div>
    <p class="claims">Vegan • Gluten Free • Organic<br>Allergy Friendly • Fair Trade</p>
    <div class="ornament-row" role="img" aria-label="Tribal border ornament"></div>
    <p class="origin-lead">Locally made in</p>
    <p class="origin">Austin Texas</p>
    <div class="ornament-row" role="img" aria-label="Tribal border ornament"></div>
    <p class="address">418 West Cobbler Ridge Rd<br>#207 Austin TX 78745</p>
    <div class="ornament-row" role="img" aria-label="Tribal border ornament"></div>
    <p class="contact">willowbendsweetsatx.com<br>512 368 4175<br>willowbendsweets</p>
  </article>

  <article class="sticker sticker--teal">
    <div class="flavour">Maple Hearts</div>
    <div class="flavour-bar"></div>
    <div class="flavour-rule"></div>
    <div class="brand-row">
      <div class="ornament-side" role="img" aria-label="Tribal spiral ornament"></div>
      <h2 class="brand">Willow<br>Bend<br>Sweets</h2>
      <div class="ornament-side" role="img" aria-label="Tribal spiral ornament"></div>
    </div>
    <p class="claims">Vegan • Gluten Free • Organic<br>Allergy Friendly • Fair Trade</p>
    <div class="ornament-row" role="img" aria-label="Tribal border ornament"></div>
    <p class="origin-lead">Locally made in</p>
    <p class="origin">Austin Texas</p>
    <div class="ornament-row" role="img" aria-label="Tribal border ornament"></div>
    <p class="address">418 West Cobbler Ridge Rd<br>#207 Austin TX 78745</p>
    <div class="ornament-row" role="img" aria-label="Tribal border ornament"></div>
    <p class="contact">willowbendsweetsatx.com<br>512 368 4175<br>willowbendsweets</p>
  </article>

  <article class="sticker sticker--yellow">
    <div class="flavour">Maple Hearts</div>
    <div class="flavour-bar"></div>
    <div class="flavour-rule"></div>
    <div class="brand-row">
      <div class="ornament-side" role="img" aria-label="Tribal spiral ornament"></div>
      <h2 class="brand">Willow<br>Bend<br>Sweets</h2>
      <div class="ornament-side" role="img" aria-label="Tribal spiral ornament"></div>
    </div>
    <p class="claims">Vegan • Gluten Free • Organic<br>Allergy Friendly • Fair Trade</p>
    <div class="ornament-row" role="img" aria-label="Tribal border ornament"></div>
    <p class="origin-lead">Locally made in</p>
    <p class="origin">Austin Texas</p>
    <div class="ornament-row" role="img" aria-label="Tribal border ornament"></div>
    <p class="address">418 West Cobbler Ridge Rd<br>#207 Austin TX 78745</p>
    <div class="ornament-row" role="img" aria-label="Tribal border ornament"></div>
    <p class="contact">willowbendsweetsatx.com<br>512 368 4175<br>willowbendsweets</p>
  </article>

  <article class="sticker sticker--kraft">
    <div class="flavour">Pecan Praline Bites</div>
    <div class="flavour-bar"></div>
    <div class="flavour-rule"></div>
    <div class="brand-row">
      <div class="ornament-side" role="img" aria-label="Tribal spiral ornament"></div>
      <h2 class="brand">Willow<br>Bend<br>Sweets</h2>
      <div class="ornament-side" role="img" aria-label="Tribal spiral ornament"></div>
    </div>
    <p class="claims">Vegan • Gluten Free • Organic<br>Allergy Friendly • Fair Trade</p>
    <div class="ornament-row" role="img" aria-label="Tribal border ornament"></div>
    <p class="origin-lead">Locally made in</p>
    <p class="origin">Austin Texas</p>
    <div class="ornament-row" role="img" aria-label="Tribal border ornament"></div>
    <p class="address">418 West Cobbler Ridge Rd<br>#207 Austin TX 78745</p>
    <div class="ornament-row" role="img" aria-label="Tribal border ornament"></div>
    <p class="contact">willowbendsweetsatx.com<br>512 368 4175<br>willowbendsweets</p>
  </article>

</main>
</body>
</html>
```